Design Challege - Simplify a Complex Message

We have a new website design, but one of the pages presents a particular problem.

Our company does ERP implementations. We have developed a proprietary approach to these implementations based on the idea that you must get eight (and only eight) things right. These eight things are listed below, summarized in one or two words each:

1. Value
2. Capability
3. Functionality
4. Data
5. Technology
6. Change Leadership
7. Quality
8. Governance

Each of these eight things can be summarized in a short paragraph, but when you combine all eight summaries with a brief introductory text, the result is a lot of text - so much text that the casual surfer may be overwhelmed by it.

The winning design will find an engaging way to present the information in a way that presents a high-level summary, using icons and one- or two-word descriptions above but revealing more information when clicked.

Our current design for this information, with a paragraph describing the eight elements in a table, is included as an upload in PDF and Microsoft Word formats. We are looking for a creative way to display these eight things, showing the detail only when the user wants to see it.

The website is being built in WordPress, using Elementor as a page builder.

We will implement (code) the page, but the winner will be asked to specify the widget or other add-in if one is required.

The design does not need to include a header or footer, we have those.

Target Market(s)

Business executives working in technology

Industry/Entity Type

Any

Number of Pages Required

1 page

Font styles to use
Sans Serif

Requirements
Must have
• A design for the body of the page, but not the header or footer.
Nice to have
• Unique icons or images appropriate for each of the eight things.
Should not have
• A lot of text on one page

```html
<!DOCTYPE html>
<html lang="en">
<head>
<meta charset="utf-8">
<title>ERP Implementations</title>
<link href="https://fonts.googleapis.com/css2?family=Poppins:wght@400;500;600&display=swap" rel="stylesheet">
<style>
  :root {
    --brand: #1a9fe0;
    --ink: #333333;
    --white: #ffffff;
    --paper: #ffffff;
  }
  * { box-sizing: border-box; margin: 0; padding: 0; }
  html, body { width: 1200px; height: 966px; overflow: hidden; background: var(--paper); }
  body { font-family: "Poppins", sans-serif; position: relative; }
  .page-title {
    position: absolute; top: 32px; left: 0; width: 1200px;
    text-align: center; color: var(--brand); font-weight: 600; font-size: 42px; line-height: 56px;
  }
  .intro {
    position: absolute; top: 122px; left: 80px; width: 1040px;
    text-align: center; color: var(--ink); font-size: 21.5px; line-height: 34.3px; font-weight: 400;
  }
  .pillar {
    position: absolute; width: 272px; height: 225px; color: var(--white); text-align: center;
  }
  .pillar-shape { position: absolute; inset: 0; }
  .pillar-shape polygon { fill: var(--brand); }
  .pillar-icon {
    position: absolute; top: 9px; left: 0; width: 272px; height: 56px;
    display: flex; justify-content: center; align-items: center;
  }
  .pillar-icon svg { fill: var(--white); }
  .pillar-title {
    position: absolute; top: 74px; left: 0; width: 272px;
    font-weight: 500; font-size: 16px; line-height: 22px;
  }
  .pillar-text {
    position: absolute; top: 98px; left: 30px; width: 212px; height: 67px; overflow: hidden;
    font-weight: 500; font-size: 13.2px; line-height: 22.3px;
  }
  .pillar-more {
    position: absolute; top: 178px; left: 74px; width: 123px; height: 26px;
    background: var(--white); color: var(--brand); font-size: 15px; line-height: 26px; font-weight: 400;
    text-decoration: none;
  }
</style>
</head>
<body>
  <h1 class="page-title">ERP Implementations</h1>
  <p class="intro">Like the roots and branches of a tree, there are many considerations in an ERP implementation. Focus too much on the minor details, and you can lose sight of the tree.<br>In an ERP implementation, you must get eight major things right to be successful. Ignore any of them, and your implementation will fail. Get them right, and you will likely succeed.</p>

  <!-- Functionality -->
  <section class="pillar" style="left:469px;top:300px">
    <svg class="pillar-shape" viewBox="0 0 272 225"><polygon points="0,112.5 69,0 206,0 272,112.5 206,225 69,225"/></svg>
    <div class="pillar-icon"><svg width="52" height="52" viewBox="0 0 52 52"><circle cx="17" cy="34" r="11"/><circle cx="37" cy="15" r="8"/><g><rect x="14" y="19" width="6" height="30"/><rect x="2" y="31" width="30" height="6"/><rect x="14" y="19" width="6" height="30" transform="rotate(45 17 34)"/><rect x="14" y="19" width="6" height="30" transform="rotate(-45 17 34)"/><rect x="35" y="4" width="4" height="22"/><rect x="26" y="13" width="22" height="4"/><rect x="35" y="4" width="4" height="22" transform="rotate(45 37 15)"/><rect x="35" y="4" width="4" height="22" transform="rotate(-45 37 15)"/></g><circle cx="17" cy="34" r="4.5" fill="#1a9fe0"/><circle cx="37" cy="15" r="3.2" fill="#1a9fe0"/></svg></div>
    <h2 class="pillar-title">Functionality</h2>
    <p class="pillar-text">An ERP project must support required business processes, both now and in the future</p>
    <a class="pillar-more" href="#">Learn More</a>
  </section>

  <!-- Capability -->
  <section class="pillar" style="left:250px;top:427px">
    <svg class="pillar-shape" viewBox="0 0 272 225"><polygon points="0,112.5 69,0 206,0 272,112.5 206,225 69,225"/></svg>
    <div class="pillar-icon"><svg width="50" height="52" viewBox="0 0 50 52"><circle cx="25" cy="5" r="4"/><path d="M19 17a6 6 0 0 1 12 0z"/><rect x="24" y="17" width="2" height="8"/><rect x="5" y="24" width="40" height="2"/><rect x="5" y="24" width="2" height="10"/><rect x="24" y="24" width="2" height="10"/><rect x="43" y="24" width="2" height="10"/><circle cx="6" cy="39" r="4"/><circle cx="25" cy="39" r="4"/><circle cx="44" cy="39" r="4"/><path d="M0 51a6 6 0 0 1 12 0z M19 51a6 6 0 0 1 12 0z M38 51a6 6 0 0 1 12 0z"/></svg></div>
    <h2 class="pillar-title">Capability</h2>
    <p class="pillar-text">The company and the implementation team must be capable of implementing the</p>
    <a class="pillar-more" href="#">Learn More</a>
  </section>

  <!-- Data -->
  <section class="pillar" style="left:687px;top:427px">
    <svg class="pillar-shape" viewBox="0 0 272 225"><polygon points="0,112.5 69,0 206,0 272,112.5 206,225 69,225"/></svg>
    <div class="pillar-icon" style="top:5px;height:70px"><svg width="50" height="68" viewBox="0 0 50 68"><path d="M4 0h32l14 14v54h-46z"/><circle cx="14" cy="24" r="6" fill="#1a9fe0"/><rect x="25" y="20" width="3" height="10" fill="#1a9fe0"/><rect x="31" y="16" width="3" height="14" fill="#1a9fe0"/><rect x="9" y="36" width="32" height="3" fill="#1a9fe0"/><rect x="9" y="43" width="32" height="3" fill="#1a9fe0"/><rect x="9" y="50" width="32" height="3" fill="#1a9fe0"/></svg></div>
    <h2 class="pillar-title">Data</h2>
    <p class="pillar-text">ERP systems are data-hungry creatures. Please be careful before assuming that</p>
    <a class="pillar-more" href="#">Learn More</a>
  </section>

  <!-- Value -->
  <section class="pillar" style="left:31px;top:539px">
    <svg class="pillar-shape" viewBox="0 0 272 225"><polygon points="0,112.5 69,0 206,0 272,112.5 206,225 69,225"/></svg>
    <div class="pillar-icon" style="top:8px;height:62px"><svg width="66" height="60" viewBox="0 0 66 60"><path d="M33 0l33 14h-66z"/><rect x="0" y="16" width="66" height="4"/><rect x="4" y="24" width="5" height="28"/><rect x="12" y="24" width="5" height="28"/><rect x="49" y="24" width="5" height="28"/><rect x="57" y="24" width="5" height="28"/><text x="33" y="50" text-anchor="middle" font-family="Poppins, sans-serif" font-weight="600" font-size="30" fill="#fff">$</text><rect x="0" y="55" width="66" height="5"/></svg></div>
    <h2 class="pillar-title">Value</h2>
    <p class="pillar-text">The project must provide value that significantly exceeds potential project costs</p>
    <a class="pillar-more" href="#">Learn More</a>
  </section>

  <!-- Quality -->
  <section class="pillar" style="left:469px;top:542px">
    <svg class="pillar-shape" viewBox="0 0 272 225"><polygon points="0,112.5 69,0 206,0 272,112.5 206,225 69,225"/></svg>
    <div class="pillar-icon" style="top:10px;height:60px"><svg width="54" height="56" viewBox="0 0 54 56"><rect x="0" y="24" width="9" height="30" rx="2"/><path d="M13 24 L26 4 Q30 -2 33 4 L31 20 H48 Q54 20 53 27 L50 48 Q49 54 43 54 H13z"/></svg></div>
    <h2 class="pillar-title">Quality</h2>
    <p class="pillar-text">Quality is multi-dimensional, and it’s more than a measurement; it’s a</p>
    <a class="pillar-more" href="#">Learn More</a>
  </section>

  <!-- Technology -->
  <section class="pillar" style="left:905px;top:540px">
    <svg class="pillar-shape" viewBox="0 0 272 225"><polygon points="0,112.5 69,0 206,0 272,112.5 206,225 69,225"/></svg>
    <div class="pillar-icon" style="top:5px;height:56px"><svg width="54" height="52" viewBox="0 0 54 52"><rect x="0" y="0" width="54" height="52" rx="10"/><ellipse cx="30" cy="22" rx="17" ry="13" fill="#1a9fe0"/><path d="M14 32 L10 46 L24 34z" fill="#1a9fe0"/><ellipse cx="30" cy="22" rx="12" ry="8.5"/></svg></div>
    <h2 class="pillar-title" style="top:66px">Technology</h2>
    <p class="pillar-text" style="top:90px">What is the platform for the system?  Is it offered by a vendor that will be</p>
    <a class="pillar-more" href="#" style="top:171px">Learn More</a>
  </section>

  <!-- Governance -->
  <section class="pillar" style="left:250px;top:667px">
    <svg class="pillar-shape" viewBox="0 0 272 225"><polygon points="0,112.5 69,0 206,0 272,112.5 206,225 69,225"/></svg>
    <div class="pillar-icon"><svg width="58" height="54" viewBox="0 0 58 54"><rect x="24" y="0" width="10" height="9" rx="2"/><path d="M6 6h52v48h-58v-42a6 6 0 0 1 6-6zM5 13v36h48v-36z" transform="translate(0 0)"/><circle cx="19" cy="25" r="6"/><path d="M9 43a10 10 0 0 1 20 0z"/><rect x="33" y="22" width="15" height="3"/><rect x="33" y="29" width="15" height="3"/><rect x="33" y="36" width="15" height="3"/></svg></div>
    <h2 class="pillar-title">Governanace</h2>
    <p class="pillar-text">ERP projects require both management and leadership. Planning, changing plans,</p>
    <a class="pillar-more" href="#">Learn More</a>
  </section>

  <!-- Change Leadership -->
  <section class="pillar" style="left:687px;top:667px">
    <svg class="pillar-shape" viewBox="0 0 272 225"><polygon points="0,112.5 69,0 206,0 272,112.5 206,225 69,225"/></svg>
    <div class="pillar-icon" style="top:12px;height:46px"><svg width="58" height="44" viewBox="0 0 58 44"><path d="M38 0 L58 13 L38 26 V18 H18 V8 H38z"/><path d="M20 18 L0 31 L20 44 V36 H40 V26 H20z"/><path d="M38 6 L51 13 L38 20z" fill="#1a9fe0"/><path d="M20 24 L7 31 L20 38z" fill="#1a9fe0"/></svg></div>
    <h2 class="pillar-title" style="top:66px">Change Leadership</h2>
    <p class="pillar-text" style="top:90px;left:26px;width:220px">Change leadership (often called change management) considers the human side of</p>
    <a class="pillar-more" href="#" style="top:171px">Learn More</a>
  </section>
</body>
</html>
```